Song Cover Art. Song Tittle Lift The Floor

I would like a design for my songs. I'm a producer and i prouder EDM music such as Big Room House / Electro House music. Currently i have a new songs tittle name Lift The Floor and i need a cover art for my songs. I'm not sure what design i have in mind right now and i would like someone to create it for me. My DJ name is DJ Vex.
Reason: Hey, i will give sometimes for you guys to create the design for me. Please do zorvix edm cover art or brenlow - lift the floor.
Target Market(s)
Electronic Dance Music Lovers
Industry/Entity Type
House
Look and feel
Each slider illustrates characteristics of the customer's brand and the style your logo design should communicate.

```html
<!DOCTYPE html>
<html lang="en">
<head>
<meta charset="utf-8">
<title>Lift The Floor – DJ Vex</title>
<link rel="stylesheet" href="https://fonts.googleapis.com/css2?family=Barlow+Condensed:wght@600&display=swap">
<style>
  :root {
    --bg-lilac: #b48eb2;
    --title-yellow: #f3e97e;
    --title-pink: #e83e82;
    --title-green: #36d09f;
    --badge-grey: #5d5d5d;
    --badge-text: #c4c4c4;
    --art-pink: #d9286f;
    --art-green: #22a57a;
  }
  html, body {
    margin: 0;
    padding: 0;
    width: 1200px;
    height: 1200px;
    overflow: hidden;
    background: var(--bg-lilac);
  }
  .cover {
    position: relative;
    width: 1200px;
    height: 1200px;
    background: var(--bg-lilac);
    overflow: hidden;
  }
  .hero-illustration {
    position: absolute;
    z-index: 1;
    left: 285px;
    top: 312px;
    width: 360px;
    height: 888px;
    opacity: 0.55;
    background: linear-gradient(180deg, var(--art-pink) 0%, var(--art-pink) 55%, var(--art-green) 100%);
  }
  .cover-type {
    position: absolute;
    z-index: 2;
    inset: 0;
    width: 1200px;
    height: 1200px;
    font-family: "Barlow Condensed", "Arial Narrow", sans-serif;
    font-weight: 600;
  }
  .title-lift { fill: var(--title-yellow); }
  .title-the { fill: var(--title-pink); }
  .title-floor { fill: var(--title-green); }
  .artist-badge { fill: var(--badge-grey); }
  .artist-name { fill: var(--badge-text); }
</style>
</head>
<body>
  <main class="cover">
    <div class="hero-illustration" role="img" aria-label="Illustration of a raised clenched fist breaking free from a green chain with a yellow spark"></div>
    <svg class="cover-type" viewBox="0 0 1200 1200" xmlns="http://www.w3.org/2000/svg">
      <text class="title-lift" x="24" y="312" font-size="430" textLength="822" lengthAdjust="spacingAndGlyphs">LIFT</text>
      <rect class="artist-badge" x="892" y="0" width="270" height="276"/>
      <text class="artist-name" x="1027" y="210" font-size="168" text-anchor="middle" textLength="216" lengthAdjust="spacingAndGlyphs">DJ Vex</text>
      <text class="title-the" x="0" y="726" font-size="585" textLength="1120" lengthAdjust="spacingAndGlyphs">THE</text>
      <text class="title-floor" x="16" y="1180" font-size="617" textLength="1164" lengthAdjust="spacingAndGlyphs">FLOOR</text>
    </svg>
  </main>
</body>
</html>
```